Book cover

I need a design for a book cover. Light back ground. On the front page a world enveloped by COVID-19 to which a stream of antibodies is going. Preferably waterpaint design.

Colors
0054AA
0677BA
7BADD7
CADEEF
E8F1F8
F0912C
F2A743
F7CA91
FBE8D2
FDF5EE

```html
<!DOCTYPE html>
<html lang="en">
<head>
<meta charset="utf-8">
<title>Antibody Based Treatment for SARS CoV-2 — Book Cover Wrap</title>
<link href="https://fonts.googleapis.com/css2?family=Montserrat:wght@500;600;700;800&display=swap" rel="stylesheet">
<style>
  :root {
    --stage: #e6e7e9;
    --blue-deep: #0054AA;
    --blue: #0677BA;
    --blue-soft: #7BADD7;
    --blue-pale: #CADEEF;
    --blue-mist: #E8F1F8;
    --navy: #1d2f57;
    --green-pale: #d9efc4;
    --lime-pale: #eef6cf;
    --spine-shade: rgba(29, 47, 87, 0.06);
  }
  * { margin: 0; padding: 0; box-sizing: border-box; }
  html, body { width: 800px; height: 1200px; overflow: hidden; background: var(--stage); }
  .page {
    position: relative;
    width: 800px;
    height: 1200px;
    overflow: hidden;
    font-family: "Montserrat", sans-serif;
  }
  .cover-wrap {
    position: absolute;
    left: 20px;
    top: 352px;
    width: 760px;
    height: 496px;
    overflow: hidden;
    background: linear-gradient(160deg, var(--blue-soft) 0%, var(--blue-pale) 30%, var(--blue-mist) 55%, var(--green-pale) 82%, var(--lime-pale) 100%);
  }
  .panel { position: absolute; top: 0; height: 100%; }
  .panel-back { left: 0; width: 312px; }
  .panel-spine {
    left: 312px;
    width: 30px;
    background: var(--spine-shade);
    border-left: 1px solid rgba(255,255,255,0.35);
    border-right: 1px solid rgba(255,255,255,0.35);
  }
  .panel-front { left: 342px; width: 418px; }

  .antibody-stream, .globe, .virus-cluster { position: absolute; display: block; }
  .antibody-stream { left: 20px; top: -10px; width: 330px; height: 240px; }
  .globe { left: 0; top: 150px; width: 520px; height: 520px; }
  .virus-cluster { left: 400px; top: 140px; width: 250px; height: 360px; }

  .spine-text {
    position: absolute;
    left: 312px;
    top: 0;
    width: 30px;
    height: 100%;
    display: flex;
    align-items: center;
    justify-content: space-between;
    writing-mode: vertical-rl;
    padding: 40px 0;
    font-size: 9px;
    font-weight: 700;
    color: var(--navy);
    white-space: nowrap;
  }
  .spine-title { letter-spacing: 0.2px; }
  .spine-author { font-weight: 600; }

  .title-block {
    position: absolute;
    left: 479px;
    top: 60px;
    color: var(--navy);
  }
  .title-kicker { font-size: 14px; font-weight: 700; line-height: 1.2; }
  .title-lead { font-size: 30px; font-weight: 700; line-height: 1.15; }
  .title-main {
    font-size: 70px;
    font-weight: 800;
    line-height: 0.95;
    color: var(--blue-deep);
    margin-top: 2px;
  }
  .author {
    position: absolute;
    left: 540px;
    top: 364px;
    font-size: 11px;
    font-weight: 700;
    color: var(--navy);
  }
</style>
</head>
<body>
<main class="page">
  <section class="cover-wrap">
    <div class="panel panel-back"></div>
    <div class="panel panel-spine"></div>
    <div class="panel panel-front"></div>

    <svg class="antibody-stream" viewBox="0 0 330 240" role="img" aria-label="Watercolour stream of Y-shaped antibodies flowing toward the globe">
      <defs>
        <radialGradient id="streamTone" cx="50%" cy="45%" r="55%">
          <stop offset="0%" stop-color="#2f5fb8" stop-opacity="0.5"/>
          <stop offset="100%" stop-color="#2f5fb8" stop-opacity="0"/>
        </radialGradient>
      </defs>
      <ellipse cx="165" cy="120" rx="165" ry="115" fill="url(#streamTone)"/>
    </svg>

    <svg class="globe" viewBox="0 0 520 520" role="img" aria-label="Watercolour painted Earth globe with blue oceans and green continents">
      <defs>
        <radialGradient id="globeTone" cx="55%" cy="40%" r="65%">
          <stop offset="0%" stop-color="#b7d877"/>
          <stop offset="45%" stop-color="#5fa4d8"/>
          <stop offset="100%" stop-color="#2f7cc4"/>
        </radialGradient>
      </defs>
      <circle cx="260" cy="260" r="255" fill="url(#globeTone)"/>
    </svg>

    <svg class="virus-cluster" viewBox="0 0 250 360" role="img" aria-label="Watercolour coronavirus particles around the globe">
      <defs>
        <radialGradient id="virusTone" cx="50%" cy="50%" r="55%">
          <stop offset="0%" stop-color="#2f6fc4" stop-opacity="0.55"/>
          <stop offset="100%" stop-color="#2f6fc4" stop-opacity="0"/>
        </radialGradient>
      </defs>
      <ellipse cx="125" cy="180" rx="120" ry="175" fill="url(#virusTone)"/>
    </svg>

    <div class="spine-text">
      <span class="spine-title">Antibody Based Treatment for SARS CoV-2</span>
      <span class="spine-author">Rohan Mehtani</span>
    </div>

    <header class="title-block">
      <p class="title-kicker">Antibody Based</p>
      <p class="title-lead">Treatment for</p>
      <h1 class="title-main">SARS<br>CoV-2</h1>
    </header>

    <p class="author">Rohan Mehtani</p>
  </section>
</main>
</body>
</html>
```